One of a kind service business!

We are the only ocean freight auditing company in the entire world that does what we do. We provide a innovative service in auditing our clients invoices for billing errors as it relates to the import and export of their products anywhere in the world. We'd like to retain the current logo - but we are open to any interesting concepts that can complete the card.

Target Market(s)

C-Level and Senior Financial executives

Industry/Entity Type

Auditing

Requirements
Must have

• ONE SIDED ONLY
Should not have
• no cartoonish images

```html
<!DOCTYPE html>
<html lang="en">
<head>
<meta charset="utf-8">
<title>Harborline Review – Business Card</title>
<link rel="stylesheet" href="https://fonts.googleapis.com/css2?family=Arimo:ital,wght@0,400;0,700;1,700&display=swap">
<style>
  :root {
    --backdrop: #e9e6e1;
    --card-top: #007ab2;
    --card-mid: #004a85;
    --card-bottom: #000b38;
    --ink: #ffffff;
    --rule: #2a9ad6;
    --mark: #7fd0f2;
    --motif: rgba(120, 190, 230, 0.10);
  }
  * { margin: 0; padding: 0; box-sizing: border-box; }
  html, body {
    width: 1200px; height: 811px; overflow: hidden;
    background: var(--backdrop);
    font-family: "Arimo", Arial, sans-serif;
    color: var(--ink);
  }
  .card {
    position: absolute; left: 50px; top: 73px;
    width: 1100px; height: 664px; overflow: hidden;
    background: linear-gradient(to bottom, var(--card-top) 0%, var(--card-mid) 55%, var(--card-bottom) 100%);
  }
  .card__motif {
    position: absolute; left: 30px; top: 20px; width: 1040px; height: 620px;
    border-radius: 50%;
    background: radial-gradient(ellipse at center, var(--motif) 0%, rgba(120,190,230,0.04) 60%, transparent 72%);
  }
  .brand {
    position: absolute; left: 41px; top: 48px;
    display: flex; align-items: center; gap: 16px;
  }
  .brand__square { width: 40px; height: 40px; background: var(--mark); }
  .brand__name { font-size: 48px; font-weight: 700; letter-spacing: 1px; line-height: 1; }
  .person__name {
    position: absolute; left: 106px; top: 186px;
    font-size: 41px; font-weight: 700; font-style: italic;
    text-shadow: 2px 3px 6px rgba(0,0,0,0.45);
  }
  .person__rule {
    position: absolute; left: 445px; right: 0; top: 230px;
    height: 1px; background: var(--rule);
  }
  .person__title {
    position: absolute; right: 108px; top: 225px;
    font-size: 43px; font-weight: 700; font-style: italic;
    text-shadow: 2px 3px 6px rgba(0,0,0,0.45);
  }
  .address {
    position: absolute; left: 104px; top: 314px;
    font-size: 30px; font-weight: 400;
  }
  .contacts {
    position: absolute; left: 104px; top: 368px;
    font-size: 27px; line-height: 38px;
    border-collapse: collapse;
  }
  .contacts td { padding: 0; }
  .contacts__label { width: 154px; }
  .footer-link {
    position: absolute; top: 580px;
    font-size: 30px; font-weight: 700; font-style: italic;
  }
  .footer-link--email { left: 44px; }
  .footer-link--web { right: 40px; }
</style>
</head>
<body>
  <div class="card">
    <div class="card__motif" role="img" aria-label="Faint globe motif in the card background"></div>

    <div class="brand">
      <span class="brand__square"></span>
      <span class="brand__name">Harborline Review</span>
    </div>

    <div class="person__name">Daniel Moravec</div>
    <div class="person__rule"></div>
    <div class="person__title">CEO</div>

    <div class="address">Brno Riverside - Lodni 18 - Czech Republic 60200</div>

    <table class="contacts">
      <tr><td class="contacts__label">Phone</td><td>: +420 555 010 143</td></tr>
      <tr><td class="contacts__label">USA</td><td>: +1 555 014 2290</td></tr>
      <tr><td class="contacts__label">Mobile</td><td>: +420 555 017 364</td></tr>
      <tr><td class="contacts__label">Fax</td><td>: +420 555 010 200</td></tr>
    </table>

    <div class="footer-link footer-link--email">danielm@harborline.example</div>
    <div class="footer-link footer-link--web">www.harborline.example</div>
  </div>
</body>
</html>
```